Tallowbrook Aesthetic Medic is the title and the name of the business

Chatterleaf advertising: keep
To those dimensions

Aimed at Caucasian women between the ages of 18 - 60 interested in beauty and cosmetic injectables. Will be boosted on chatterleaf which is my advertising platform.

Name: Tallowbrook Aesthetic Medic
0491 570 318

Forehead $58
Frown lines $116
Crows feet $116
Lip fillers $380

I would like to have a beautiful girl that suits the picture.

Target Market(s)

Females between 18 - 60 interested in Lumiset and cosmetic fillers
Prefer Caucasian as that's the majority of population

Industry/Entity Type

Beauty Salon

Font styles to use
Serif
Script

Colors
e667a6
eea4c8
f9d9e8
fee18a
fbf289
fbee3d
cadf82
cedeed
85cae6

Requirements
Must have
• Name: Tallowbrook Aesthetic Medic
• Phone number: 0491 570 381
• Prices:
• Forehead $58
• Frown lines $116
• Crows feet $116
• Lip fillers $380
• Picture of female that is very beautiful
Nice to have
• Not a cartoon or anything else that's not a real picture of a female
Should not have
• No cartoon pictures. Proper picture of women

```html
<!DOCTYPE html>
<html lang="en">
<head>
<meta charset="utf-8">
<title>Tallowbrook Aesthetic Medic – Ad Banners</title>
<link rel="stylesheet" href="https://fonts.googleapis.com/css2?family=Roboto+Condensed:wght@700&family=Open+Sans:wght@300;700;800&display=swap">
<style>
  :root {
    --canvas: #e4e5e7;
    --ink: #0f0d0e;
    --magenta: #a5096c;
    --bar: #3b3435;
    --white: #ffffff;
    --cta: #fcc318;
    --cta-ink: #2a1a10;
    --skin-light: #f1d3bf;
    --skin-mid: #d9a88c;
    --skin-shadow: #5a3a30;
  }
  * { box-sizing: border-box; margin: 0; padding: 0; }
  html, body {
    width: 1200px; height: 1200px; overflow: hidden;
    background: var(--canvas);
  }
  .canvas { position: relative; width: 1200px; height: 1200px; }
  .banner { position: absolute; overflow: hidden; background: var(--ink); }
  .banner--square { left: 350px; top: 187px; width: 500px; height: 416px; }
  .banner--wide   { left: 261px; top: 663px; width: 678px; height: 351px; }

  .banner__photo {
    position: absolute; top: 0; right: 0; bottom: 0;
    background: radial-gradient(ellipse at 60% 45%, var(--skin-light) 0%, var(--skin-mid) 55%, var(--skin-shadow) 100%);
  }
  .banner--square .banner__photo { left: 246px; }
  .banner--wide .banner__photo { left: 231px; }

  .banner__panel { position: absolute; left: 0; top: 0; }

  .brand {
    position: absolute;
    font-family: "Open Sans", sans-serif; font-weight: 800; color: var(--white);
    line-height: 1.05;
  }
  .brand__line { display: block; }
  .banner--square .brand { top: 18px; left: 25px; width: 215px; font-size: 30px; }
  .banner--wide .brand { top: 12px; left: 31px; width: 190px; font-size: 26px; }

  .phone-bar {
    position: absolute; left: 0; background: var(--bar);
    display: flex; align-items: center; gap: 8px;
    font-family: "Roboto Condensed", sans-serif; font-weight: 700; color: var(--white);
  }
  .phone-bar svg { fill: var(--white); flex: none; }
  .banner--square .phone-bar { top: 193px; width: 207px; height: 39px; padding-left: 14px; font-size: 23px; }
  .banner--square .phone-bar svg { width: 22px; height: 18px; }
  .banner--wide .phone-bar { top: 162px; width: 227px; height: 34px; padding-left: 30px; font-size: 21px; }
  .banner--wide .phone-bar svg { width: 20px; height: 16px; }

  .price-list { position: absolute; list-style: none; font-family: "Open Sans", sans-serif; color: var(--white); }
  .price-list__item { display: flex; }
  .price-list__name { font-weight: 300; }
  .price-list__price { font-weight: 700; }
  .banner--square .price-list { left: 17px; top: 248px; font-size: 22px; }
  .banner--square .price-list__item { height: 28px; line-height: 28px; }
  .banner--square .price-list__name { width: 145px; }
  .banner--wide .price-list { left: 31px; top: 208px; font-size: 19px; }
  .banner--wide .price-list__item { height: 24px; line-height: 24px; }
  .banner--wide .price-list__name { width: 123px; }

  .cta {
    position: absolute; display: flex; align-items: center; justify-content: center;
    font-family: "Open Sans", sans-serif; font-weight: 800; color: var(--cta-ink);
  }
  .cta svg { position: absolute; inset: 0; width: 100%; height: 100%; fill: var(--cta); }
  .cta span { position: relative; }
  .banner--square .cta { left: 50px; top: 375px; width: 121px; height: 30px; font-size: 14px; }
  .banner--wide .cta { left: 67px; top: 316px; width: 104px; height: 24px; font-size: 12px; }
</style>
</head>
<body>
<main class="canvas">

  <section class="banner banner--square">
    <div class="banner__photo" role="img" aria-label="Close-up photograph of a beautiful woman with glossy pink lips and manicured nails touching her cheek"></div>
    <svg class="banner__panel" width="500" height="416" viewBox="0 0 500 416" aria-hidden="true">
      <polygon points="0,123 246,154 241,416 0,416" fill="var(--magenta)"/>
    </svg>
    <h1 class="brand">
      <span class="brand__line">Tallowbrook</span>
      <span class="brand__line">Aesthetic</span>
      <span class="brand__line">Medic</span>
    </h1>
    <div class="phone-bar">
      <svg viewBox="0 0 24 20" aria-hidden="true"><path d="M2 6c0-3 4-5 10-5s10 2 10 5v2h-6V6c0-1-2-1.5-4-1.5S8 5 8 6v2H2zM6 9h12l3 9H3z"/></svg>
      <span>0491 570 381</span>
    </div>
    <ul class="price-list">
      <li class="price-list__item"><span class="price-list__name">Forehead</span><span class="price-list__price">$58</span></li>
      <li class="price-list__item"><span class="price-list__name">Frown lines</span><span class="price-list__price">$116</span></li>
      <li class="price-list__item"><span class="price-list__name">Crows feet</span><span class="price-list__price">$116</span></li>
      <li class="price-list__item"><span class="price-list__name">Lip fillers</span><span class="price-list__price">$380</span></li>
    </ul>
    <div class="cta">
      <svg viewBox="0 0 121 30" preserveAspectRatio="none" aria-hidden="true"><polygon points="8,0 121,0 113,30 0,30"/></svg>
      <span>CHECK NOW</span>
    </div>
  </section>

  <section class="banner banner--wide">
    <div class="banner__photo" role="img" aria-label="Photograph of a beautiful woman with glossy pink lips and manicured nails touching her cheek"></div>
    <svg class="banner__panel" width="678" height="351" viewBox="0 0 678 351" aria-hidden="true">
      <polygon points="0,102 231,133 228,351 0,351" fill="var(--magenta)"/>
    </svg>
    <h2 class="brand">
      <span class="brand__line">Tallowbrook</span>
      <span class="brand__line">Aesthetic</span>
      <span class="brand__line">Medic</span>
    </h2>
    <div class="phone-bar">
      <svg viewBox="0 0 24 20" aria-hidden="true"><path d="M2 6c0-3 4-5 10-5s10 2 10 5v2h-6V6c0-1-2-1.5-4-1.5S8 5 8 6v2H2zM6 9h12l3 9H3z"/></svg>
      <span>0491 570 381</span>
    </div>
    <ul class="price-list">
      <li class="price-list__item"><span class="price-list__name">Forehead</span><span class="price-list__price">$58</span></li>
      <li class="price-list__item"><span class="price-list__name">Frown lines</span><span class="price-list__price">$116</span></li>
      <li class="price-list__item"><span class="price-list__name">Crows feet</span><span class="price-list__price">$116</span></li>
      <li class="price-list__item"><span class="price-list__name">Lip fillers</span><span class="price-list__price">$380</span></li>
    </ul>
    <div class="cta">
      <svg viewBox="0 0 104 24" preserveAspectRatio="none" aria-hidden="true"><polygon points="7,0 104,0 97,24 0,24"/></svg>
      <span>CHECK NOW</span>
    </div>
  </section>

</main>
</body>
</html>
```